Classy business card for accounting firm

We're looking for a new business card for our accounting firm. Our logo was designed by Brandloom, so all of the design info we would like to use has been provided. The specific font provided isn't required to be used.

We want the card to look classy and elegent. Probably more minimalistic, but still with some pops of color.

The options we would like to include on the card are as follows:
1. Main office phone line
2. Direct phone line
3. Email address
4. Website URL
5. Name
6. Title (CEO, President, etc.)
7. Firm Address

The design and card should be double sided!!! The drop down box in the project brief for some reason is defaulting to single sided. Not sure why this is happening.

Thanks!

Contact Information for Business Card

The options we would like to include on the card are as follows: 1. Main office phone line 2. Direct phone line 3. Email address 4. Website URL 5. Name 6. Title (CEO, President, etc.) 7. Firm Address

Requirements
Must have
• Card must be double sided.

```html
<!DOCTYPE html>
<html lang="en">
<head>
<meta charset="utf-8">
<title>Ledgerline Associates – Business Card</title>
<link rel="stylesheet" href="https://fonts.googleapis.com/css2?family=Open+Sans:wght@400;600&display=swap">
<style>
  :root {
    --canvas: #e4e4e6;
    --paper: #f5f5f5;
    --orange: #ee7a1f;
    --orange-deep: #c9571a;
    --orange-light: #f59a45;
    --green: #8db83a;
    --ink: #2b2b2b;
    --grey: #555555;
    --white: #ffffff;
  }
  * { margin: 0; padding: 0; box-sizing: border-box; }
  html, body { width: 1200px; height: 780px; overflow: hidden; }
  body {
    background: var(--canvas);
    font-family: "Open Sans", Arial, sans-serif;
    color: var(--ink);
  }
  .sheet {
    position: relative;
    width: 1200px;
    height: 780px;
    display: flex;
    align-items: center;
    justify-content: center;
    gap: 40px;
  }
  .card {
    position: relative;
    width: 540px;
    height: 310px;
    overflow: hidden;
    box-shadow: 0 6px 18px rgba(0,0,0,0.18);
  }

  /* Wordmark */
  .wordmark {
    display: flex;
    align-items: center;
    gap: 10px;
    font-family: "Open Sans", Arial, sans-serif;
    font-weight: 600;
    font-size: 24px;
    line-height: 1;
    white-space: nowrap;
    color: var(--grey);
  }
  .wordmark__dot {
    width: 14px; height: 14px;
    border-radius: 50%;
    background: var(--orange);
    flex: none;
  }

  /* Front */
  .card--front { background: var(--paper); }
  .card--front .wordmark {
    position: absolute;
    top: 62px;
    left: 214px;
  }

  .person {
    position: absolute;
    top: 140px;
    left: 40px;
    width: 210px;
  }
  .person__name {
    font-size: 26px;
    font-weight: 600;
    line-height: 1.1;
    white-space: nowrap;
  }
  .person__first { color: var(--orange); }
  .person__last { color: var(--green); }
  .person__title { margin-top: 4px; font-size: 16px; color: var(--ink); }

  .divider {
    position: absolute;
    top: 128px;
    left: 262px;
    width: 1px;
    height: 110px;
    background: var(--ink);
  }

  .contacts {
    position: absolute;
    top: 132px;
    left: 284px;
    list-style: none;
    font-size: 16px;
    line-height: 24px;
  }
  .contacts__item { display: flex; align-items: center; gap: 8px; white-space: nowrap; }
  .contacts__icon { width: 13px; height: 13px; flex: none; }

  .address-band {
    position: absolute;
    left: 0; right: 0; bottom: 0;
    height: 40px;
    background: var(--orange);
    color: var(--white);
    font-size: 16px;
    line-height: 40px;
    padding-left: 40px;
    white-space: nowrap;
  }

  /* Back */
  .card--back { background: var(--orange); }
  .back-pattern {
    position: absolute;
    inset: 0;
    background: linear-gradient(110deg, var(--orange-deep) 0%, var(--orange) 55%, var(--orange-light) 100%);
  }
  .card--back .wordmark {
    position: absolute;
    top: 50%;
    left: 50%;
    transform: translate(-50%, -50%);
    font-size: 26px;
    color: var(--white);
  }
  .card--back .wordmark__dot { background: var(--white); }
</style>
</head>
<body>
<main class="sheet">

  <section class="card card--front" aria-label="Business card front">
    <div class="wordmark"><span class="wordmark__dot"></span>Ledgerline Associates</div>

    <div class="person">
      <div class="person__name"><span class="person__first">Mara</span> <span class="person__last">Kovalenko</span></div>
      <div class="person__title">Managing Director</div>
    </div>

    <div class="divider"></div>

    <ul class="contacts">
      <li class="contacts__item">
        <svg class="contacts__icon" viewBox="0 0 14 14" aria-hidden="true"><rect x="3.5" y="1" width="7" height="12" rx="1.2" fill="none" stroke="#8db83a" stroke-width="1.3"/><circle cx="7" cy="11" r="0.7" fill="#8db83a"/></svg>
        (555) 014-2758
      </li>
      <li class="contacts__item">
        <svg class="contacts__icon" viewBox="0 0 14 14" aria-hidden="true"><path d="M3 1.5l2.2 2.3-1.2 1.6c.8 1.8 2 3 3.8 3.8l1.6-1.2 2.3 2.2-1.4 2.2C6 12 2 8 1 2.9z" fill="#ee7a1f"/></svg>
        (555) 014-2222
      </li>
      <li class="contacts__item">
        <svg class="contacts__icon" viewBox="0 0 14 14" aria-hidden="true"><rect x="1" y="3" width="12" height="8.5" rx="1" fill="#8db83a"/><path d="M1.5 3.5L7 8l5.5-4.5" fill="none" stroke="#fff" stroke-width="1"/></svg>
        info@ledgerline.com
      </li>
      <li class="contacts__item">
        <svg class="contacts__icon" viewBox="0 0 14 14" aria-hidden="true"><circle cx="7" cy="7" r="6" fill="#ee7a1f"/><path d="M1 7h12M7 1c-2.5 3-2.5 9 0 12M7 1c2.5 3 2.5 9 0 12" fill="none" stroke="#fff" stroke-width="0.8"/></svg>
        www.ledgerline.com
      </li>
    </ul>

    <div class="address-band">2048 Harlow Ct #101, Easton, FL 32901, USA</div>
  </section>

  <section class="card card--back" aria-label="Business card back">
    <div class="back-pattern" role="img" aria-label="Repeating pattern of small brand symbols in deep and light orange tones"></div>
    <div class="wordmark"><span class="wordmark__dot"></span>Ledgerline Associates</div>
  </section>

</main>
</body>
</html>
```